Webdesign für Entwickler von onlinebasierten Terminformularen
Zielgruppe
Deutsch:
Wir sind ein Startup, das über die Seite Buchwerk.de zukünftig folgenden Service anbietet: Unternehmer können sehr flexibel (selbst) gestaltete Terminformulare erstellen und auf Ihrer Website einbinden. Kunden können dann diese Termine buchen und bekommen dann Erinnerungs-Mails und SMS.
Zielgruppe: Dienstleister wie Fotografen, Friseure, Versicherungsvertreter, Masseure, Restaurants, Arztpraxen. Also alle, die darauf angewiesen sind, dass vereinbarte Termine eingehalten werden und die die Terminvereinbarung vereinfachen wollen. Also weniger per Telefon, mehr über die eigene Website.
Englisch:
We are a start up, that is going to offer this services on the Website Buchwerk.de :
Companies can create highly flexible (self-designed) appointment forms and integrate them on their website. Customer can book appointments and will get an reminding email and SMS.
Target group: Service providers such as photographers, hairdressers, insurance agents, masseurs, restaurants, medical offices. So all those who depend on meeting agreed appointments and who want to simplify the appointment. Less by telephone, more over their own website.
Aufgabenstellung
Übersichtlichkeit, genug Weißraum, deutliche, große Überschriften, Seriös aber gerne frische Farben bei einzelnen Elementen (z.B. bei Icons oder bei Handlungsaufforderungs-Buttons), Trennlinien, Inhalte auf den Punkt.
Logo-Entwurf anbei (wird gerade hier über entwurfsmarkt.de ebenfalls erstellt/optimiert, siehe #418276) sagt das wesentliche aus.
Buchwerk soll also ein sehr nützliches Tool sein, das jeder schnell versteht. Daher muss auch die Website sehr übersichtlich und klar aufgebaut werden. Die wesentlichen Aussagen/Menüpunkte finden sich auf der Startseite (bzw. im Hauptmenü, siehe grober Entwurf anbei).
- frische Farben (z.B. grün, orange, gelb)
- seröse Farben/Grauwerte (z.B. blau, grau, schwarz)
- Hauptmenü/Metanavigation/Footer-Bereich
Das Design und das Teaser-Bild (Frau mit Hammer) auf dem Entwurf anbei (seite1_mit_teaser_entwurf2.jpg) sind nur als grobe Ideen (Richtung) zu verstehen. Die Startseite muss also keine Teaser-Bilder enthalten.
Der Entwurf anbei soll lediglich die ungefähre Richtung mit den angedachten Menüpunkten verdeutlichen.
Übersichtlich und modern finden wir z.B. https://talkrunde.com/de (viel Weißraum, farbige Icons, Infos übersichtlich dargeboten, lächelnde Gesichter) und übrigens auch https://www.entwurfsmarkt.de.
Bitte entwerfen Sie (erstmal) drei Seiten:
- Startseite
- Funktionen/Preis (Beispiel auf https://talkrunde.com/de/tools Und/oder in Tabellenform wie auf https://talkrunde.com/de/pricing/ siehe Content-Plan anbei)
- Über Buchwerk (Über uns, siehe Content-Plan anbei)
Der Content-Plan soll das Projekt verdeutlichen.
Anmerkung von unserem Programmierer: Praktisch wäre eine Basis auf Bootstrap. Dies ist aber keine Pflicht! Das Design/die Idee geht vor :-)
1zu1-Folgeaufträge (für dieses und andere Projekte im Bereich Webdesign, Flyer, CorporateDesign, Grafiken) sind sehr wahrsc..

```html
<!DOCTYPE html>
<html lang="de">
<head>
<meta charset="utf-8">
<title>Buchwerk – Über uns</title>
<link href="https://fonts.googleapis.com/css2?family=Jost:wght@400;500;600&display=swap" rel="stylesheet">
<style>
:root{
  --ink:#6b777b;
  --ink-soft:#8a9498;
  --green:#8dc63f;
  --green-tint:#e8f2de;
  --slate:#737d80;
  --slate-dark:#5f696d;
  --meta:#6b767a;
  --panel:#f6f6f6;
  --tile:#f4f5f4;
  --white:#fff;
}
*{box-sizing:border-box;margin:0;padding:0}
html,body{width:1200px;height:3545px;overflow:hidden}
body{font-family:'Jost',sans-serif;color:var(--ink);background:var(--white);position:relative}
.abs{position:absolute}
/* meta bar */
.meta-bar{left:0;top:0;width:1200px;height:32px;background:var(--meta)}
.meta-links{right:218px;top:9px;font-size:9px;color:#e6e9ea;display:flex;gap:8px;align-items:center}
.meta-links .sep{opacity:.5}
/* main nav */
.main-nav{left:0;top:32px;width:1200px;height:52px;background:var(--white);border-bottom:1px solid #eee}
.brand{display:flex;align-items:center;gap:6px;font-size:22px;font-weight:500;color:var(--ink)}
.brand .mark{width:16px;height:16px;background:var(--green)}
.nav-item{top:21px;font-size:10px;color:var(--ink)}
.nav-item.active{color:var(--ink)}
.nav-item.active::after{content:"";position:absolute;left:0;right:0;top:18px;height:2px;background:var(--green)}
.btn-outline-sm{left:890px;top:12px;width:91px;height:28px;border:2px solid var(--green);border-radius:14px;font-size:10px;display:flex;align-items:center;justify-content:center;color:var(--ink)}
/* hero */
.hero{left:0;top:84px;width:1200px;height:212px;background:var(--slate);color:var(--white);text-align:center}
.hero h1{position:absolute;top:76px;width:100%;font-size:25px;font-weight:500}
.hero p{position:absolute;top:117px;width:100%;font-size:15px;font-weight:400}
/* text blocks */
.h2{font-size:25px;font-weight:500;line-height:32px;color:var(--ink)}
.copy{font-size:11.5px;line-height:24px;color:var(--ink-soft);width:340px}
.btn-outline{width:188px;height:49px;border:2px solid var(--green);font-size:11.5px;font-weight:500;display:flex;align-items:center;justify-content:center;color:var(--ink)}
/* features */
.feature{left:626px;width:354px;height:47px;background:var(--tile);display:flex;align-items:center;padding-left:16px;gap:12px;font-size:12.5px;color:var(--ink)}
.feature.current{background:var(--green-tint)}
.feature svg{width:22px;height:22px;flex:none}
/* photos */
.photo{background:linear-gradient(135deg,#c9d2d8,#8d9aa4 55%,#5d6e80)}
/* strengths */
.strengths{left:0;top:1803px;width:1200px;height:480px;background:var(--panel)}
.center-h{width:1200px;text-align:center}
.lead{font-size:11.5px;line-height:24px;color:var(--ink-soft);text-align:center;width:1200px}
.card{top:2039px;width:179px;height:145px;background:var(--white);box-shadow:0 2px 6px rgba(0,0,0,.06);text-align:center}
.card svg{position:absolute;left:62px;top:34px;width:55px;height:55px}
.card span{position:absolute;top:108px;left:0;width:100%;font-size:13px;color:var(--ink)}
/* goals */
.goal-num{width:55px;height:55px;border-radius:50%;background:var(--white);box-shadow:0 2px 8px rgba(0,0,0,.1);display:flex;align-items:center;justify-content:center;color:var(--green);font-size:20px;font-weight:500}
.goal-title{font-size:12.5px;color:var(--ink)}
.goal-text{font-size:9px;line-height:17.5px;color:var(--ink-soft);width:265px}
/* cta */
.cta{left:0;top:2925px;width:1200px;height:406px;background:radial-gradient(ellipse at 40% 55%,#6a6055,#3d4246 55%,#2f3538);color:var(--white);text-align:center}
.cta h2{position:absolute;top:122px;width:100%;font-size:26px;font-weight:500}
.cta p{position:absolute;top:162px;width:100%;font-size:15.5px;line-height:24px}
.btn-solid{left:422px;top:232px;width:354px;height:48px;background:var(--green);color:var(--white);font-size:11.5px;font-weight:500;display:flex;align-items:center;justify-content:center}
/* footer */
.footer-top{left:0;top:3331px;width:1200px;height:68px;background:var(--slate)}
.footer-bottom{left:0;top:3399px;width:1200px;height:146px;background:var(--slate-dark);color:#e4e8e9}
.f-head{top:19px;font-size:9px;font-weight:500}
.f-link{font-size:9px;line-height:17.5px;color:#d2d8da}
.lang-pill{left:213px;top:52px;width:145px;height:30px;border:1px solid #d2d8da;border-radius:15px;font-size:9px;display:flex;align-items:center;padding-left:20px;gap:16px}
.btn-footer{left:801px;top:88px;width:180px;height:34px;background:var(--green);color:var(--white);font-size:10px;font-weight:500;display:flex;align-items:center;justify-content:center}
</style>
</head>
<body>

<!-- meta bar -->
<div class="abs meta-bar">
  <div class="abs meta-links"><span>Kontakt</span><span class="sep">|</span><span>DE ⌄</span><span class="sep">|</span><span>Zu Klickwahl wechseln</span></div>
</div>

<!-- main nav -->
<header class="abs main-nav">
  <div class="abs brand" style="left:237px;top:12px"><span class="mark"></span>Buchwerk</div>
  <div class="abs nav-item active" style="left:377px">Funktionen / Preis</div>
  <div class="abs nav-item" style="left:497px">Help-Center</div>
  <div class="abs nav-item" style="left:590px">Über Uns</div>
  <div class="abs nav-item" style="left:669px">Blog</div>
  <div class="abs nav-item" style="left:853px">Login</div>
  <div class="abs btn-outline-sm">Konto erstellen</div>
</header>

<!-- hero -->
<section class="abs hero">
  <h1>Wir sind Buchwerk</h1>
  <p>Lesen Sie mehr zu Uns und Buchwerk.</p>
</section>

<!-- what is special -->
<h2 class="abs h2" style="left:212px;top:398px">Was ist das besondere<br>an Buchwerk?</h2>
<p class="abs copy" style="left:212px;top:498px">Lorem ipsum dolor sit amet, consetetur sadipscing elitr, sed diam nonumy eirmod tempor invidunt ut labore et dolore magna aliquyam erat, sed diam voluptua. At vero eos et accusam et justo duo dolores et ea rebum. Stet clita kasd</p>
<div class="abs btn-outline" style="left:212px;top:632px">Mehr erfahren</div>

<div class="abs feature" style="top:365px"><svg viewBox="0 0 22 22" fill="none" stroke="#8dc63f" stroke-width="1.4"><rect x="4" y="5" width="15" height="12"/><rect x="2" y="7" width="15" height="12" fill="#fff"/><path d="M4 17l4-4 3 3 2-2 3 3"/></svg>Umfragen mit Teaser-Foto / Videoportal-Video</div>
<div class="abs feature" style="top:425px"><svg viewBox="0 0 22 22" fill="none" stroke="#8dc63f" stroke-width="1.4"><rect x="3" y="3" width="16" height="5"/><rect x="3" y="10" width="16" height="3"/><rect x="3" y="15" width="16" height="4" fill="#8dc63f"/></svg>Formular-Generator</div>
<div class="abs feature current" style="top:486px"><svg viewBox="0 0 22 22" fill="none" stroke="#6b777b" stroke-width="1.5"><rect x="3" y="4" width="16" height="15"/><path d="M3 8h16M7 2v4M15 2v4M7 13l3 3 5-5"/></svg>Termin-Assistent (Wizzard)</div>
<div class="abs feature" style="top:545px"><svg viewBox="0 0 22 22" fill="none" stroke="#8dc63f" stroke-width="1.4"><circle cx="6" cy="15" r="3"/><circle cx="11" cy="6" r="2"/><path d="M9 14h11M14 10v8M11 8v3"/></svg>Branchenspezifische Vorlagen</div>
<div class="abs feature" style="top:605px"><svg viewBox="0 0 22 22" fill="none" stroke="#8dc63f" stroke-width="1.4"><rect x="3" y="3" width="16" height="16" rx="1"/><circle cx="10" cy="10" r="3.5"/><path d="M12.5 12.5l4 4"/></svg>Termin-Verwaltung und Terminübersicht</div>
<div class="abs feature" style="top:665px"><svg viewBox="0 0 22 22" fill="none" stroke="#8dc63f" stroke-width="1.4"><rect x="1" y="5" width="9" height="6"/><rect x="12" y="5" width="9" height="6"/><path d="M11 11v8M8 16l3 3 3-3"/></svg>Teilnehmerliste als CSV / PDF-Export</div>

<!-- who stands behind -->
<div class="abs" style="left:0;top:800px;width:1200px;height:428px;background:var(--panel)"></div>
<div class="abs photo" role="img" aria-label="Foto: vier junge Kolleginnen und Kollegen arbeiten gemeinsam am Laptop" style="left:0;top:800px;width:560px;height:428px;background:linear-gradient(120deg,#e9eef2,#b8c4ce 45%,#6f8497 80%,#4c5c6c)"></div>
<h2 class="abs h2" style="left:634px;top:872px">Wer steht hinter<br>Buchwerk?</h2>
<p class="abs copy" style="left:634px;top:972px">Lorem ipsum dolor sit amet, consetetur sadipscing elitr, sed diam nonumy eirmod tempor invidunt ut labore et dolore magna aliquyam erat, sed diam voluptua. At vero eos et accusam et justo duo dolores et ea rebum. Stet clita kasd</p>
<div class="abs btn-outline" style="left:634px;top:1105px">Mehr erfahren</div>

<!-- reason -->
<h2 class="abs h2" style="left:212px;top:1378px">Was war der Grund, warum wir<br>Buchwerk entwickelt haben?</h2>
<p class="abs copy" style="left:212px;top:1466px">Lorem ipsum dolor sit amet, consetetur sadipscing elitr, sed diam nonumy eirmod tempor invidunt ut labore et dolore magna aliquyam erat, sed diam voluptua. At vero eos et accusam et justo duo dolores et ea rebum. Stet clita kasd</p>
<div class="abs btn-outline" style="left:212px;top:1598px">Mehr erfahren</div>
<div class="abs photo" role="img" aria-label="Foto: junger Mann im blauen Hemd arbeitet an einem Tablet" style="left:630px;top:1316px;width:347px;height:398px;background:linear-gradient(160deg,#dfe3e4,#b7bec2 40%,#5e7fae 70%,#3f5f8f)"></div>

<!-- strengths -->
<section class="abs strengths"></section>
<h2 class="abs h2 center-h" style="left:0;top:1872px">Was sind unsere Stärken?</h2>
<p class="abs lead" style="left:0;top:1922px">Lorem ipsum dolor sit amet, consetetur sadipscing elitr, sed diam nonumy eirmod tempor<br>invidunt ut labore et dolore magna aliquyam erat, sed diam voluptua.</p>

<div class="abs card" style="left:213px"><svg viewBox="0 0 55 55" fill="none" stroke="#8dc63f" stroke-width="3"><circle cx="30" cy="24" r="18"/><path d="M30 13v12h9"/><path d="M14 44c-8-5-8-11-3-11 2 0 3 2 3 2s1-2 3-2c5 0 5 6-3 11z" fill="#8dc63f" stroke="none"/></svg><span>Stärke Lorem Ipsum</span></div>
<div class="abs card" style="left:410px"><svg viewBox="0 0 55 55" fill="none" stroke="#8dc63f" stroke-width="3"><rect x="6" y="10" width="38" height="34"/><path d="M6 19h38M15 5v9M35 5v9"/><path d="M30 48V37l9-7 9 7v11z" fill="#fff"/><rect x="36" y="41" width="6" height="7" fill="#8dc63f" stroke="none"/></svg><span>Stärke Lorem Ipsum</span></div>
<div class="abs card" style="left:607px"><svg viewBox="0 0 55 55" fill="none" stroke="#8dc63f" stroke-width="3"><circle cx="30" cy="24" r="18"/><path d="M30 13v12h9"/><path d="M14 44c-8-5-8-11-3-11 2 0 3 2 3 2s1-2 3-2c5 0 5 6-3 11z" fill="#8dc63f" stroke="none"/></svg><span>Stärke Lorem Ipsum</span></div>
<div class="abs card" style="left:804px"><svg viewBox="0 0 55 55" fill="none" stroke="#8dc63f" stroke-width="3"><circle cx="30" cy="24" r="18"/><path d="M30 13v12h9"/><path d="M14 44c-8-5-8-11-3-11 2 0 3 2 3 2s1-2 3-2c5 0 5 6-3 11z" fill="#8dc63f" stroke="none"/></svg><span>Stärke Lorem Ipsum</span></div>

<!-- goals -->
<h2 class="abs h2 center-h" style="left:0;top:2365px">Was sind unsere Ziele?</h2>
<p class="abs lead" style="left:0;top:2416px">Lorem ipsum dolor sit amet, consetetur sadipscing elitr, sed diam nonumy eirmod tempor<br>invidunt ut labore et dolore magna aliquyam erat, sed diam voluptua.</p>

<div class="abs goal-num" style="left:213px;top:2541px">1</div>
<div class="abs goal-title" style="left:293px;top:2530px">Hier steht das erste Ziel</div>
<p class="abs goal-text" style="left:293px;top:2555px">Lorem ipsum dolor sit amet, consetetur sadipscing elitr, sed diam nonumy eirmod tempor invidunt ut labore et dolore magna aliquyam erat, sed diam voluptua.</p>

<div class="abs goal-num" style="left:647px;top:2541px">2</div>
<div class="abs goal-title" style="left:727px;top:2530px">Hier steht das zweite Ziel</div>
<p class="abs goal-text" style="left:727px;top:2555px">Lorem ipsum dolor sit amet, consetetur sadipscing elitr, sed diam nonumy eirmod tempor invidunt ut labore et dolore magna aliquyam erat, sed diam voluptua.</p>

<div class="abs goal-num" style="left:213px;top:2656px">3</div>
<div class="abs goal-title" style="left:293px;top:2645px">Hier steht das dritte Ziel</div>
<p class="abs goal-text" style="left:293px;top:2670px">Lorem ipsum dolor sit amet, consetetur sadipscing elitr, sed diam nonumy eirmod tempor invidunt ut labore et dolore magna aliquyam erat, sed diam voluptua.</p>

<div class="abs goal-num" style="left:647px;top:2656px">4</div>
<div class="abs goal-title" style="left:727px;top:2645px">Hier steht das vierte Ziel</div>
<p class="abs goal-text" style="left:727px;top:2670px">Lorem ipsum dolor sit amet, consetetur sadipscing elitr, sed diam nonumy eirmod tempor invidunt ut labore et dolore magna aliquyam erat, sed diam voluptua.</p>

<div class="abs btn-outline" style="left:506px;top:2800px">Mehr erfahren</div>

<!-- call to action -->
<section class="abs cta" role="img" aria-label="Unscharfes Hintergrundfoto: Menschen an einem Arbeitstisch">
  <h2>Holen Sie sich jetzt Buchwerk</h2>
  <p>Profitieren Sie jetzt von Buchwerk und sichern Sie sich<br>alle Vorteile. Verwalten Sie jetzt Ihre Termine.</p>
  <div class="abs btn-solid">Jetzt kostenlos Konto erstellen</div>
</section>

<!-- footer -->
<footer>
  <div class="abs footer-top">
    <div class="abs brand" style="left:213px;top:20px;color:#fff"><span class="mark" style="background:#fff"></span>Buchwerk</div>
  </div>
  <div class="abs footer-bottom">
    <div class="abs f-head" style="left:213px">© 2018 Alle Rechte vorbehalten</div>
    <div class="abs lang-pill"><span>Sprachauswahl</span><span>DE ⌄</span></div>

    <div class="abs f-head" style="left:493px">Sonstiges</div>
    <div class="abs f-link" style="left:493px;top:37px">Home<br>Kontakt<br>Newsletter<br>Webinare</div>

    <div class="abs f-head" style="left:574px">Benutzer</div>
    <div class="abs f-link" style="left:574px;top:37px">Login<br>Konto erstellen</div>

    <div class="abs f-head" style="left:670px">Rechtliches</div>
    <div class="abs f-link" style="left:670px;top:37px">Impressum<br>AGB<br>Datenschutz<br>Sitemap</div>

    <div class="abs f-head" style="left:798px">Bewertungen durch Klickwahl.de</div>
    <div class="abs f-link" style="left:798px;top:37px;width:180px;font-size:8px;line-height:12px">Verknüpfen Sie jetzt Buchwerk mit Klickwahl.de und profitieren Sie von vertrauensvollen Usern und Transparenz.</div>
    <div class="abs btn-footer">zu Klickwahl.de wechseln</div>
  </div>
</footer>

</body>
</html>
```